Brightstone Roofing Business Card

This is my current business card. But I’d like to make some changes. Somewhere on the card I’d like to list some of the services we offer. Maybe on the back? But I’d still like to keep the red. White and black modern look.

-residential & commercial roofing
-Roof Repairs & Maintenance
-Storm Damage & Insurance Claims specialist
-Christmas Lights and permanent Christmas lights
Fencing. Windows. Gutters. Siding. Sheetrock, painting.

```html
<!DOCTYPE html>
<html lang="en">
<head>
<meta charset="utf-8">
<title>Brightstone Roofing Business Card</title>
<link rel="stylesheet" href="https://fonts.googleapis.com/css2?family=Lato:wght@400;700;900&family=Oswald:wght@400;500&display=swap">
<style>
  :root {
    --red: #e3141b;
    --black: #121214;
    --white: #ffffff;
    --grey: #6b6b6b;
    --stage: #2b2c2f;
  }
  * { margin: 0; padding: 0; box-sizing: border-box; }
  html, body { width: 1200px; height: 952px; overflow: hidden; }
  body {
    background: var(--stage);
    font-family: "Lato", sans-serif;
    position: relative;
  }
  .card {
    position: absolute;
    left: 250px;
    width: 700px;
    height: 400px;
    overflow: hidden;
  }
  .card-front { top: 56px; background: var(--white); }
  .card-back { top: 496px; background: var(--black); color: var(--white); }

  .edge-stripe {
    position: absolute;
    left: 0; right: 0;
    bottom: 30px;
    height: 4px;
    display: flex;
  }
  .edge-stripe span { flex: 1; }
  .card-front .edge-stripe span:nth-child(odd) { background: var(--black); }
  .card-front .edge-stripe span:nth-child(even) { background: var(--red); }
  .card-back .edge-stripe span:nth-child(odd) { background: var(--white); }
  .card-back .edge-stripe span:nth-child(even) { background: var(--red); }

  .brand {
    position: absolute;
    display: flex;
    align-items: center;
    gap: 18px;
  }
  .brand-mark {
    width: 96px; height: 96px;
    border-radius: 50%;
    background: var(--red);
    flex: none;
  }
  .brand-name {
    font-weight: 900;
    font-size: 34px;
    line-height: 1.05;
    letter-spacing: 1px;
    text-transform: uppercase;
  }
  .card-front .brand { left: 150px; top: 58px; }
  .card-front .brand-name { color: var(--red); }
  .card-back .brand { left: 40px; top: 120px; }
  .card-back .brand-name { color: var(--white); font-size: 26px; }

  .person {
    position: absolute;
    left: 60px; top: 215px;
  }
  .person-name {
    font-size: 32px;
    font-weight: 400;
    letter-spacing: 1px;
    color: var(--black);
    text-transform: uppercase;
  }
  .person-name .surname { color: var(--red); font-weight: 700; }
  .person-role {
    margin-top: 4px;
    font-size: 15px;
    color: var(--grey);
    letter-spacing: 1px;
    text-transform: uppercase;
    text-align: right;
  }

  .contacts {
    position: absolute;
    left: 360px; top: 215px;
    list-style: none;
  }
  .contacts li {
    display: flex;
    align-items: center;
    gap: 12px;
    font-size: 16px;
    color: var(--grey);
    margin-bottom: 12px;
  }
  .contacts svg { width: 20px; height: 20px; flex: none; }

  .services {
    position: absolute;
    left: 370px; top: 70px;
    list-style: none;
    font-family: "Oswald", sans-serif;
    font-size: 17px;
    line-height: 1.75;
  }
  .services li::before {
    content: "•";
    color: var(--red);
    margin-right: 6px;
  }
  .services .row { display: flex; gap: 16px; }
  .services .row span::before {
    content: "•";
    color: var(--red);
    margin-right: 6px;
  }
  .services .row-item::before { content: none; margin: 0; }
</style>
</head>
<body>

<section class="card card-front" aria-label="Business card front">
  <div class="brand">
    <div class="brand-mark"></div>
    <div class="brand-name">Brightstone<br>Roofing Co.</div>
  </div>

  <div class="person">
    <p class="person-name">Dale <span class="surname">Morgan</span></p>
    <p class="person-role">Owner</p>
  </div>

  <ul class="contacts">
    <li>
      <svg viewBox="0 0 20 20"><rect width="20" height="20" rx="3" fill="#121214"/><path d="M6 4.5l2 .3.8 2.6-1.3 1a7 7 0 0 0 3.6 3.6l1-1.3 2.6.8.3 2-1.6 1.3C9 14.6 5.4 11 4.7 6.1z" fill="#fff"/></svg>
      555-014-2298
    </li>
    <li>
      <svg viewBox="0 0 20 20"><rect width="20" height="20" rx="3" fill="#121214"/><rect x="4" y="6" width="12" height="8" fill="none" stroke="#fff" stroke-width="1.4"/><path d="M4 6l6 5 6-5" fill="none" stroke="#fff" stroke-width="1.4"/></svg>
      dale@brightstoneroofing.co
    </li>
    <li>
      <svg viewBox="0 0 20 20"><rect width="20" height="20" rx="3" fill="#121214"/><path d="M6 4l8 6-3.5.6 2 4-1.6.8-2-4L6 14z" fill="#fff"/></svg>
      www.brightstoneroofing.co
    </li>
  </ul>

  <div class="edge-stripe"><span></span><span></span><span></span><span></span><span></span><span></span><span></span></div>
</section>

<section class="card card-back" aria-label="Business card back">
  <div class="brand">
    <div class="brand-mark"></div>
    <div class="brand-name">Brightstone<br>Roofing Co.</div>
  </div>

  <ul class="services">
    <li>residential &amp; commercial roofing</li>
    <li>Roof Repairs &amp; Maintenance</li>
    <li>Storm Damage &amp; Insurance Claims specialist</li>
    <li>Christmas Lights and permanent Christmas lights</li>
    <li class="row-item"><span class="row"><span>Fencing</span><span>Windows</span><span>Gutters</span><span>Siding</span></span></li>
    <li class="row-item"><span class="row"><span>Sheetrock</span><span>painting</span></span></li>
  </ul>

  <div class="edge-stripe"><span></span><span></span><span></span><span></span><span></span><span></span><span></span></div>
</section>

</body>
</html>
```